Business Card and Logo Color Scheme Design Contest

We are starting a new company called Lone Ridge Structural Partners and already have a logo however, the colors for the logo itself are not final and COULD be changed. I'm hoping to move AWAYfrom the gold color in the card and the logo as it seems a bit outdated. What we need help with is to find what our business color scheme will be, and then incorporate those colors into both the logo and the business card design itself. We also want to make sure we are known as "LRS" so in the future we can just refer to ourselves as "LRS" and not Lone Ridge Structural Partners. That being said, I would like to make a slight change to the logo to somehow include the letters "LRS." The logo used in the front of the card design MUST ALSO include the words "Firm No. 64307" within the logo. My vision is for the front of the card to have the information shown in the attached image. For the back of the card, I'm hoping to have something very simple. I'm envisioning a solid color with either the website (www.bridgemarkplans.com) and a simplified version of the logo. I've attached an example but I'm looking for a complete redesign. I'm looking for a slick, modern and simple design.

Industry/Entity Type

Civil Engineer

Contact Information for Business Card

Logo
Firm No. 64307
Rowan Pettibone, PE
Chief Operating Officer
Email:rpettibone@bridgemarkplans.com
Ph: 555.201.0142 | D: 555.201.0178 | M:555.309.0263
4187 W. Kellingham, Cedar Hollow, Texas 75999
www.bridgemarkplans.com

Requirements
Must have
• Logo
Contact Info
Nice to have
• "LRS" Incorporated in the design
Should not have
• The current color scheme

```html
<!DOCTYPE html>
<html lang="en">
<head>
<meta charset="utf-8">
<title>LRS Business Card</title>
<link href="https://fonts.googleapis.com/css2?family=Montserrat:wght@400;500;700;800&display=swap" rel="stylesheet">
<style>
  :root {
    --backdrop: #2a2a28;
    --card-white: #f4f4f2;
    --card-black: #161616;
    --ink: #111111;
    --ink-soft: #5a5a5a;
    --silver: #c9c9c9;
    --silver-dim: #8c8c8c;
  }
  * { margin: 0; padding: 0; box-sizing: border-box; }
  html, body { width: 1200px; height: 1029px; overflow: hidden; }
  body {
    background: var(--backdrop);
    font-family: "Montserrat", Arial, sans-serif;
    position: relative;
  }
  .card {
    position: absolute;
    width: 525px;
    height: 300px;
    border-radius: 2px;
    box-shadow: 0 18px 40px rgba(0,0,0,0.45);
  }
  .card-front {
    left: 60px; top: 480px;
    background: var(--card-white);
    color: var(--ink-soft);
  }
  .holder-name {
    position: absolute; left: 38px; top: 34px;
    font-size: 23px; font-weight: 500; letter-spacing: 1px;
    text-transform: uppercase; color: var(--ink-soft);
  }
  .holder-name .credential { font-size: 14px; letter-spacing: 0.5px; }
  .holder-title {
    position: absolute; left: 38px; top: 66px;
    font-size: 13px; font-weight: 500; letter-spacing: 1px;
    text-transform: uppercase; color: var(--ink-soft);
  }
  .rule-top {
    position: absolute; left: 0; top: 62px; width: 34px;
    border-top: 1.5px solid var(--ink);
  }
  .rule-main {
    position: absolute; left: 250px; right: 0; top: 88px;
    border-top: 1.5px solid var(--ink);
  }
  .phone-list {
    position: absolute; left: 38px; top: 112px;
    list-style: none; font-size: 12px; line-height: 22px;
  }
  .phone-list li { display: flex; align-items: center; gap: 9px; }
  .phone-list .tag { font-weight: 700; color: var(--ink); font-size: 11px; }
  .icon { width: 11px; height: 11px; fill: var(--ink); flex: none; }
  .brand {
    position: absolute; right: 34px; top: 120px; width: 170px;
    color: var(--ink);
  }
  .brand-mark {
    display: flex; align-items: center; gap: 8px;
    font-size: 46px; font-weight: 800; line-height: 1; letter-spacing: 1px;
  }
  .brand-mark .dot { width: 12px; height: 12px; background: var(--ink); }
  .brand-name {
    margin-top: 4px; font-size: 9px; font-weight: 700; line-height: 11px;
    text-transform: uppercase; letter-spacing: 0.8px;
  }
  .contact-foot {
    position: absolute; right: 34px; bottom: 26px;
    list-style: none; font-size: 12px; line-height: 22px; text-align: right;
  }
  .contact-foot li { display: flex; align-items: center; justify-content: flex-end; gap: 9px; }
  .card-back {
    left: 615px; top: 230px;
    background: var(--card-black);
  }
  .back-mark {
    position: absolute; left: 0; right: 0; top: 70px;
    text-align: center; font-size: 108px; font-weight: 800;
    letter-spacing: 4px; color: var(--silver); line-height: 1;
  }
  .back-url {
    position: absolute; left: 0; right: 0; bottom: 58px;
    text-align: center; font-size: 15px; letter-spacing: 4px;
    text-transform: uppercase; color: var(--silver-dim);
  }
</style>
</head>
<body>
  <svg width="0" height="0" style="position:absolute">
    <symbol id="i-phone" viewBox="0 0 24 24"><path d="M6.6 10.8a15.1 15.1 0 0 0 6.6 6.6l2.2-2.2a1 1 0 0 1 1-.25 11.4 11.4 0 0 0 3.6.57 1 1 0 0 1 1 1V20a1 1 0 0 1-1 1A17 17 0 0 1 3 4a1 1 0 0 1 1-1h3.5a1 1 0 0 1 1 1c0 1.25.2 2.45.57 3.57a1 1 0 0 1-.25 1z"/></symbol>
    <symbol id="i-mobile" viewBox="0 0 24 24"><path d="M7 1h10a2 2 0 0 1 2 2v18a2 2 0 0 1-2 2H7a2 2 0 0 1-2-2V3a2 2 0 0 1 2-2zm0 3v15h10V4z"/></symbol>
    <symbol id="i-mail" viewBox="0 0 24 24"><path d="M2 5h20v14H2zm2 2v.5l8 5 8-5V7z"/></symbol>
    <symbol id="i-pin" viewBox="0 0 24 24"><path d="M12 1a8 8 0 0 0-8 8c0 6 8 14 8 14s8-8 8-14a8 8 0 0 0-8-8zm0 11a3 3 0 1 1 0-6 3 3 0 0 1 0 6z"/></symbol>
  </svg>

  <section class="card card-front">
    <div class="rule-top"></div>
    <h1 class="holder-name">Rowan Pettibone, <span class="credential">PE</span></h1>
    <p class="holder-title">Chief Operating Officer</p>
    <div class="rule-main"></div>

    <ul class="phone-list">
      <li><svg class="icon"><use href="#i-phone"/></svg>555.201.0142</li>
      <li><svg class="icon"><use href="#i-phone"/></svg>555.201.0178 <span class="tag">(Direct)</span></li>
      <li><svg class="icon"><use href="#i-mobile"/></svg>555.309.0263</li>
    </ul>

    <div class="brand">
      <div class="brand-mark"><span class="dot"></span>LRS</div>
      <p class="brand-name">Lone Ridge<br>Structural Partners<br>Firm No. 64307</p>
    </div>

    <ul class="contact-foot">
      <li>rpettibone@bridgemarkplans.com<svg class="icon"><use href="#i-mail"/></svg></li>
      <li>4187 W. Kellingham, Cedar Hollow, Texas 75999<svg class="icon"><use href="#i-pin"/></svg></li>
    </ul>
  </section>

  <section class="card card-back">
    <div class="back-mark">LRS</div>
    <p class="back-url">www.bridgemarkplans.com</p>
  </section>
</body>
</html>
```